If everything digital fails, here's what to do

Hi, I would like a poster / infographic of a list of practical actions people could take in case the internet stops working. I've put together a list of 8 areas, with the situation for each, and the mitigation actions folks can take - I need it presented in a clear and aesthetically pleasing way. I will send you the file with the full text so you can include it all

Target Market(s)

General population, but likely people who are safety conscious and want to protect themselves and learn more about what to do to be tech literate and prepared

Industry/Entity Type

Tech / Cyber / Public safety / Civic tech

Font styles to use
Sans Serif

Requirements
Must have
• It's a lot of text, so I think the important thing is to have it all in one poster, or in a series of similar pages
Nice to have
• I would like it to be a bit brooding, but also elicit competence and that some experts have thought about this and it will all be okay
Should not have
• I don't want it to look cartoonish, or cheap - less is more is sort of what I'm looking for

```html
<!DOCTYPE html>
<html lang="en">
<head>
<meta charset="utf-8">
<title>Communications – If everything digital fails</title>
<link rel="stylesheet" href="https://fonts.googleapis.com/css2?family=Barlow:wght@700;800&family=Barlow+Semi+Condensed:wght@400;600;700&display=swap">
<style>
  :root {
    --deep-teal: #215a66;
    --ribbon-teal: #45b0bb;
    --fold-teal: #1d7a7c;
    --steel-blue: #4a78be;
    --card-grey: #8f9aa5;
    --card-sky: #76b4d0;
    --ink: #1f5565;
    --white: #ffffff;
  }
  * { box-sizing: border-box; margin: 0; padding: 0; }
  html, body { width: 848px; height: 1200px; overflow: hidden; background: var(--white); }
  body { position: relative; font-family: "Barlow Semi Condensed", "Arial Narrow", sans-serif; }

  .title-band {
    position: absolute; left: 149px; top: 44px; width: 699px; height: 70px;
    background: var(--deep-teal);
  }
  .title {
    position: absolute; left: 180px; width: 585px; top: 44px; height: 70px;
    text-align: center; line-height: 72px;
    font-family: "Barlow", sans-serif; font-weight: 800; font-size: 62px;
    color: var(--white); letter-spacing: 1px;
  }
  .title-badge { position: absolute; left: 55px; top: 23px; width: 110px; height: 110px; }

  .ribbon { position: absolute; left: 112px; top: 151px; width: 620px; height: 50px; }
  .ribbon-text {
    position: absolute; left: 112px; top: 151px; width: 600px; height: 41px;
    line-height: 42px; text-align: center; color: var(--white);
    font-weight: 700; font-size: 17.5px; letter-spacing: 0.1px;
    text-shadow: 1px 1px 1px rgba(0,0,0,0.45);
  }

  .column-label {
    position: absolute; top: 187px; width: 195px; height: 44px;
    line-height: 44px; text-align: center; color: var(--white);
    font-weight: 700; font-size: 25px;
    text-shadow: 1px 1px 1px rgba(0,0,0,0.3);
  }
  .column-label.actions { left: 139px; background: var(--deep-teal); }
  .column-label.refresh { left: 505px; background: var(--steel-blue); }

  .panel { position: absolute; top: 237px; height: 794px; border-radius: 26px; }
  .panel.actions { left: 51px; width: 389px; background: var(--deep-teal); }
  .panel.refresh { left: 452px; width: 346px; background: var(--steel-blue); }

  .card {
    position: absolute; border-radius: 8px;
    font-size: 16.6px; line-height: 23.2px; padding: 7px 7px 0 7px;
  }
  .actions .card {
    left: 12px; width: 367px; color: var(--white);
    background: linear-gradient(to bottom, var(--deep-teal) 0%, var(--card-grey) 100%);
  }
  .refresh .card {
    left: 11px; width: 326px; color: var(--ink); padding-left: 13px;
    background: linear-gradient(to bottom, #f7fafc 0%, var(--card-sky) 100%);
  }
  .row-1 { top: 17px; height: 106px; }
  .row-2 { top: 130px; height: 204px; }
  .row-3 { top: 345px; height: 108px; padding-top: 15px !important; }
  .row-4 { top: 468px; height: 93px; padding-top: 9px !important; }
  .row-5 { top: 579px; height: 172px; padding-top: 9px !important; }
  .refresh .row-5 { top: 594px; height: 157px; padding-top: 6px !important; }
</style>
</head>
<body>

<div class="title-band"></div>
<svg class="title-badge" viewBox="0 0 110 110" aria-hidden="true">
  <circle cx="55" cy="55" r="51" fill="#ffffff" stroke="#215a66" stroke-width="6"/>
  <rect x="37" y="22" width="37" height="67" rx="5" fill="#45b0bb"/>
  <rect x="41" y="30" width="29" height="46" fill="#ffffff"/>
  <rect x="51" y="25.5" width="8" height="1.6" rx="0.8" fill="#ffffff"/>
  <rect x="51" y="80" width="8" height="4.5" rx="2" fill="#ffffff"/>
</svg>
<h1 class="title">COMMUNICATIONS</h1>

<svg class="ribbon" viewBox="0 0 620 50" aria-hidden="true">
  <path d="M0 34 H27 V49 H6 Q0 49 0 43 Z" fill="#1d7a7c"/>
  <path d="M0 0 H593 L606 20.5 L593 41 H0 Z" fill="#45b0bb"/>
</svg>
<p class="ribbon-text">CELL PHONES / LAND-LINE PHONE SERVICES HAVE STOPPED WORKING</p>

<h2 class="column-label actions">What to do?</h2>
<h2 class="column-label refresh">Refresh when?</h2>

<section class="panel actions">
  <p class="card row-1">1) Buy a two-way hand-held walkie talkieand share the other with close friends.</p>
  <p class="card row-2">2) Share a ‘third space’ safe spot with close contacts in town where you know you could meet in emergency situations if yourhome was not safe to remain in. Do the same with neigh-bours and folks who live in your neighbour-hood - have a central gathering spot in your hood that you share with others so you can have a convening spot close by.</p>
  <p class="card row-3">3) Have a printed list of your close contacts’ home addresses handy, if you don’t know how to get to their places by heart.</p>
  <p class="card row-4">4) Have a list of close contacts that might still have a working landline (ie. rotary, not voip-based), or who have a satellite phone</p>
  <p class="card row-5">5) Make a list of the people in your life that you care about that may also be affected, and make sure you include individuals in your community that may be vulnerable in such a disruption (they may be older, may live alone, might need access to supply of medication).</p>
</section>

<section class="panel refresh">
  <p class="card row-1">Check to ensure your walkie talkie has working batteries every 12 months (and that you know / remember how the walkie talkie itself works)</p>
  <p class="card row-2">Have a quick reminder conversation about this with your close contacts every 12 months to ensure everyone knows that’s the plan</p>
  <p class="card row-3">Print a new such document every 12 months to ensure it stays up to date</p>
  <p class="card row-4">Remind yourself of this list and refresh it every 12 months or so</p>
  <p class="card row-5">Remind yourself of this list and refresh it every 12 months or so</p>
</section>

</body>
</html>
```